Surviving Domestic Violence Flyer

I need a flyer that "POPS" to attract participants for my research project. I have added the important information on my draft flyer.

```html
<!DOCTYPE html>
<html lang="en">
<head>
<meta charset="utf-8">
<title>Survivors of Domestic Abuse – Request for Study Participants</title>
<link rel="stylesheet" href="https://fonts.googleapis.com/css2?family=Questrial&family=Arimo:wght@400;700&display=swap">
<style>
  :root {
    --violet-deep: #8745cf;
    --violet-mid: #9a52d8;
    --violet-band: #c47be9;
    --violet-light: #d9a6f2;
    --photo-dark: #3a2418;
    --photo-warm: #8a5a68;
    --ink: #0d0612;
    --white: #ffffff;
    --glow: rgba(255,255,255,0.85);
  }
  * { box-sizing: border-box; margin: 0; padding: 0; }
  html, body { width: 930px; height: 1200px; overflow: hidden; }
  body {
    position: relative;
    background: linear-gradient(180deg, var(--violet-mid) 0%, var(--violet-deep) 100%);
    font-family: "Arimo", Arial, sans-serif;
    color: var(--ink);
  }
  .hero-photo {
    position: absolute; left: 0; top: 0; width: 930px; height: 640px;
    background:
      radial-gradient(ellipse 260px 320px at 380px 230px, #d8b3b0 0%, #b98a8c 45%, rgba(140,90,110,0) 100%),
      radial-gradient(ellipse 200px 120px at 760px 300px, rgba(240,230,255,0.7), rgba(240,230,255,0) 100%),
      linear-gradient(180deg, var(--photo-dark) 0%, var(--photo-warm) 35%, #b57ed6 70%, var(--violet-mid) 100%);
  }
  .headline {
    position: absolute; left: 0; width: 930px; text-align: center;
    font-family: "Questrial", Arial, sans-serif; color: var(--white);
    text-shadow: 0 0 10px rgba(60,20,80,0.7), 0 2px 4px rgba(0,0,0,0.5);
    line-height: 1; letter-spacing: 1px;
  }
  .headline-top { top: 352px; left: 88px; width: auto; font-size: 80px; text-align: left; }
  .headline-top small { font-size: 58px; }
  .headline-bottom { top: 428px; left: 88px; width: auto; font-size: 80px; text-align: left; padding-left: 40px; }
  .request {
    position: absolute; top: 518px; left: 0; width: 930px; text-align: center;
    font-family: "Questrial", Arial, sans-serif; font-size: 45px; color: var(--ink);
    text-shadow: 0 0 8px var(--glow);
    letter-spacing: 1px;
  }
  .study-title {
    position: absolute; top: 563px; left: 0; width: 930px; text-align: center;
    font-family: "Questrial", Arial, sans-serif; font-size: 29px; line-height: 29px; color: var(--ink);
    text-shadow: 0 0 6px var(--glow), 0 0 2px var(--white);
  }
  .criteria {
    position: absolute; top: 632px; left: 0; width: 930px; height: 200px;
    background: var(--violet-band);
    border-top: 2px solid var(--violet-light);
    border-bottom: 2px solid #a962dc;
    list-style: none; padding: 14px 20px 0 48px;
  }
  .criteria li {
    position: relative; padding-left: 18px;
    font-family: "Questrial", Arial, sans-serif; font-size: 19.5px; line-height: 24px;
    color: var(--white); text-shadow: 0 1px 3px rgba(60,10,80,0.7);
    margin-bottom: 13px;
  }
  .criteria li::before {
    content: ""; position: absolute; left: 0; top: 6px; width: 12px; height: 12px;
    border-radius: 50%; background: var(--white);
  }
  .criteria li.double { margin-bottom: 0; }
  .compensation {
    position: absolute; top: 838px; left: 0; width: 930px; text-align: center;
    font-family: "Questrial", Arial, sans-serif; font-size: 29px; color: var(--ink);
    text-shadow: 0 0 6px var(--glow);
  }
  .eligibility, .contact, .investigator {
    position: absolute; left: 0; width: 930px; text-align: center; padding: 0 60px;
    font-size: 14.5px; line-height: 16px; color: #1a0a24;
    text-shadow: 0 0 4px rgba(255,255,255,0.6);
  }
  .eligibility { top: 873px; }
  .contact { top: 920px; font-size: 15px; padding: 0 30px; }
  .investigator { top: 973px; font-size: 15px; line-height: 16px; }
  .investigator b { font-weight: 700; }
  .tear-tabs {
    position: absolute; left: 30px; top: 1040px; width: 880px; height: 160px;
    display: flex;
  }
  .tab {
    width: 40px; height: 160px; border-left: 1px solid var(--white);
    position: relative;
  }
  .tab:last-child { border-right: 1px solid var(--white); }
  .tab-text {
    position: absolute; left: 20px; top: 80px; width: 150px;
    transform: translate(-50%, -50%) rotate(-90deg);
    color: var(--white); font-size: 11.5px; line-height: 12px; text-align: center; white-space: nowrap;
  }
</style>
</head>
<body>
  <div class="hero-photo" role="img" aria-label="Close-up portrait photograph of a woman with dark hair and bangs, fading into violet light"></div>

  <h1 class="headline headline-top">SURVIVORS <small>OF</small></h1>
  <div class="headline headline-bottom">DOMESTIC ABUSE</div>

  <h2 class="request">REQUEST FOR STUDY PARTICIPANTS</h2>
  <p class="study-title">EFFICIENCY OF RESOURCES AVAILABLE<br>TO SURVIVORS OF INTIMATE PARTER ABUSE</p>

  <ul class="criteria">
    <li>ARE YOU EIGHTEEN YEARS OF AGE OR OLDER?</li>
    <li>HAVE YOU BEEN A VICTIM OF DOMESTIC VIOLENCE?</li>
    <li>HAVE YOU SOUGHT ASSISTANCE WITH ABUSE IN THE LAST 12 MONTHS?</li>
    <li class="double">ARE YOU STILL IN CONTACT WITH THE PERSON WHO ABUSED YOU? ARE YOU WILLING AND OPEN TO DISCUSSING YOUR EXPERIENCE WITH ABUSE AND YOUR ATTEMPTS TO ACCESS SERVICES OR RESOURCES?</li>
  </ul>

  <h3 class="compensation">PARTICIPANTS WILL BE COMPENSATED FOR THEIR TIME</h3>
  <p class="eligibility">If you answered yes to all of these questions, you may be eligible to participate in a study to better understand the resources needed and services expected for survivors of domestic violence.</p>
  <p class="contact">Please contact Dana Whitfield at 1(312)555-0148 or vie e-mail survivorvoicesstudy@example.com for additional information.</p>
  <p class="investigator">
    <b>Principal Investigator:</b> Dana Whitfield<br>
    <b>Institutional Affiliation:</b> Lakeshore State University, Dept. of Criminology, Law, and Justice<br>
    <b>Contact Address:</b> Post Office Box 2210, Chicago, IL, 60601
  </p>

  <div class="tear-tabs">
    <div class="tab"><span class="tab-text">Survivor Resources Study<br>1(312)555-0148</span></div>
    <div class="tab"><span class="tab-text">Survivor Resources Study<br>1(312)555-0148</span></div>
    <div class="tab"><span class="tab-text">Survivor Resources Study<br>1(312)555-0148</span></div>
    <div class="tab"><span class="tab-text">Survivor Resources Study<br>1(312)555-0148</span></div>
    <div class="tab"><span class="tab-text">Survivor Resources Study<br>1(312)555-0148</span></div>
    <div class="tab"><span class="tab-text">Survivor Resources Study<br>1(312)555-0148</span></div>
    <div class="tab"><span class="tab-text">Survivor Resources Study<br>1(312)555-0148</span></div>
    <div class="tab"><span class="tab-text">Survivor Resources Study<br>1(312)555-0148</span></div>
    <div class="tab"><span class="tab-text">Survivor Resources Study<br>1(312)555-0148</span></div>
    <div class="tab"><span class="tab-text">Survivor Resources Study<br>1(312)555-0148</span></div>
    <div class="tab"><span class="tab-text">Survivor Resources Study<br>1(312)555-0148</span></div>
    <div class="tab"><span class="tab-text">Survivor Resources Study<br>1(312)555-0148</span></div>
    <div class="tab"><span class="tab-text">Survivor Resources Study<br>1(312)555-0148</span></div>
    <div class="tab"><span class="tab-text">Survivor Resources Study<br>1(312)555-0148</span></div>
    <div class="tab"><span class="tab-text">Survivor Resources Study<br>1(312)555-0148</span></div>
    <div class="tab"><span class="tab-text">Survivor Resources Study<br>1(312)555-0148</span></div>
    <div class="tab"><span class="tab-text">Survivor Resources Study<br>1(312)555-0148</span></div>
    <div class="tab"><span class="tab-text">Survivor Resources Study<br>1(312)555-0148</span></div>
    <div class="tab"><span class="tab-text">Survivor Resources Study<br>1(312)555-0148</span></div>
    <div class="tab"><span class="tab-text">Survivor Resources Study<br>1(312)555-0148</span></div>
    <div class="tab"><span class="tab-text">Survivor Resources Study<br>1(312)555-0148</span></div>
    <div class="tab"><span class="tab-text">Survivor Resources Study<br>1(312)555-0148</span></div>
  </div>
</body>
</html>
```